Webshop for baby shoes need new design

We are an innovative company selling a one of a kind product on a market with tough competition. We are looking to step up our business and need a new design for our shop.

We are looking for recognition as well as originality. The customer must immediately be able to identify navigation, shopping cart, buy buttons etc. We want warm welcoming colors, but not too strong as to not draw attention away from the products. Retro might be interesting, if "done right".

Suggested color palette: http://huepalettemaker.example/#7k29WbQx3p8r5

We have a logo (attached), but if you have a better idea we might go for that instead. Also, a couple of product images are attached for you to use in the design.

What we do NOT want is a shop that looks like a free template (vendaForge etc). Also, while we are selling baby shoes, we don't want to use the very worn our baby pink/blue scheme, so stay clear of this, thanks.
Updates

We suggest that you use this palette, or similar: http://huepalettemaker.example/#7k29WbQx3p8r5

Project Deadline Extended
Reason: We feel that we are getting closer to finding a design that we like, but there is still a bit to go. Also we want to give the chance to any late starters to show their idea. The competition is still open.

Target Market(s)

babies and their parents

Industry/Entity Type

Shopping

Requirements
Must have
• The usual webshop elements
- shopping cart
- product listing
- product page
- buy buttons
Nice to have
• - large footer area for links, info and function (see trindel.example for an example)
- some kind of product navigation/filter (left, top or right)
- place for promotion banners

```html
<!DOCTYPE html>
<html lang="en">
<head>
<meta charset="utf-8">
<title>Tassino – Baby Shoes</title>
<link href="https://fonts.googleapis.com/css2?family=Questrial&family=Arimo:wght@400;700&display=swap" rel="stylesheet">
<style>
:root{
  --page:#f3f0e8;
  --outer:#ffffff;
  --brown:#6b4325;
  --brown-dark:#4a2e18;
  --leather-top:#c08a4e;
  --leather-bot:#9a6530;
  --wine:#7c2f3a;
  --wine-dark:#5e1f2a;
  --line:#e2d9c7;
  --card:#f6f2ea;
  --text-soft:#8a6a45;
  --dot:#c9b2b6;
}
*{box-sizing:border-box;margin:0;padding:0}
html,body{width:1200px;height:1000px;overflow:hidden;background:var(--outer)}
body{position:relative;font-family:"Questrial",sans-serif;color:var(--brown)}
.abs{position:absolute}
.page{left:84px;top:22px;width:1035px;height:951px;background:var(--page)}
.top-links{left:655px;top:30px;font-family:"Arimo",sans-serif;font-size:8px;color:var(--brown-dark);letter-spacing:.3px;display:flex;gap:10px}
.top-links .sep{color:var(--leather-bot)}
.search{left:848px;top:27px;width:128px;height:17px;border:1px solid var(--line);border-radius:3px;background:#f8f5ef}
.rule{height:0;border-top:1px dashed var(--line)}
.brand{left:226px;top:64px;display:flex;align-items:center;gap:12px}
.brand-mark{width:85px;height:60px;border-radius:8px;background:var(--leather-bot)}
.brand-name{font-size:48px;color:var(--brown);letter-spacing:1px}
.badge{left:688px;top:100px;width:116px;height:22px;border-radius:4px;background:#dfe8c9}
.cart-box{left:819px;top:64px;width:157px;height:60px;border:1px solid var(--line);border-radius:4px;background:#fbf9f4;overflow:hidden}
.cart-icon{left:8px;top:8px;width:30px;height:30px;border-radius:3px;background:#e6dccb}
.cart-count{left:8px;top:14px;width:11px;height:11px;border-radius:50%;background:var(--wine);color:#fff;font-family:"Arimo",sans-serif;font-size:7px;text-align:center;line-height:11px}
.cart-text{right:7px;top:7px;text-align:right;font-family:"Arimo",sans-serif;font-size:8px;line-height:10px;color:var(--wine)}
.cart-text b{display:block}
.cart-bar{left:0;bottom:0;width:100%;height:13px;background:var(--wine-dark);color:#f1e6e2;font-family:"Arimo",sans-serif;font-size:7.5px;text-align:right;padding-right:8px;line-height:13px}
.nav{left:84px;top:140px;width:1035px;height:44px;background:linear-gradient(var(--leather-top),var(--leather-bot));border-top:1px solid #8a5a2a;border-bottom:1px solid #7a4d22}
.nav::before,.nav::after{content:"";position:absolute;left:0;right:0;border-top:1px dashed rgba(255,230,190,.55)}
.nav::before{top:4px}.nav::after{bottom:4px}
.nav-item{top:13px;font-size:15px;letter-spacing:.5px;color:var(--brown-dark)}
.nav-div{left:712px;top:6px;width:1px;height:32px;background:rgba(80,45,15,.35)}
.slider{left:226px;top:205px;width:752px;height:364px;border:2px solid var(--line);border-radius:5px}
.hero{left:263px;top:245px;width:677px;height:281px;background:linear-gradient(160deg,#c2bcad 0%,#a59d8c 45%,#8f8674 100%)}
.hero-legs{left:480px;top:245px;width:300px;height:200px;background:linear-gradient(#9a7858,#b58e66);opacity:.55;border-radius:0 0 40px 40px}
.slogan{left:280px;top:418px;font-size:38px;color:#fff;letter-spacing:1px}
.slogan-copy{left:281px;top:463px;width:260px;font-size:13.5px;line-height:16px;color:var(--brown-dark)}
.arrow{top:372px}
.dots{left:571px;top:541px;display:flex;gap:6px}
.dots span{width:11px;height:11px;border-radius:50%;background:var(--dot)}
.dots .on{background:var(--wine-dark)}
.section-title{left:226px;top:594px;font-size:17px;letter-spacing:.5px;color:var(--brown)}
.card{top:641px;width:231px;height:300px;border:2px solid var(--line);border-radius:5px;background:var(--card);overflow:hidden}
.card-name{left:18px;top:10px;font-size:15.5px;color:var(--brown-dark);letter-spacing:.2px}
.card-desc{left:18px;top:28px;font-size:12px;color:var(--text-soft);letter-spacing:.3px}
.ribbon{right:-2px;top:-2px}
.product-img{left:15px;top:48px;width:195px;height:195px;background:#fff;border:1px solid #ece6da}
.shoe{left:25px;top:45px;width:145px;height:105px;border-radius:40% 45% 12% 14%}
.price{left:21px;top:258px;font-size:17px;color:var(--wine)}
.btn-fav{left:132px;top:253px;width:36px;height:32px;background:#fff;border:1px solid #e5ddd0;border-radius:2px}
.btn-cart{left:174px;top:253px;width:36px;height:32px;background:var(--wine);border-radius:2px}
.btn-fav svg,.btn-cart svg{position:absolute;left:8px;top:6px}
.view-more{left:930px;top:948px;font-size:10px;color:var(--text-soft);text-decoration:underline}
</style>
</head>
<body>
<div class="abs page"></div>

<div class="abs top-links"><span>MY ACCOUNT</span><span class="sep">|</span><span>MY WISHLIST</span><span class="sep">|</span><span>LOG OUT</span></div>
<div class="abs search"><svg class="abs" style="left:5px;top:3px" width="10" height="10" viewBox="0 0 10 10"><circle cx="4" cy="4" r="3" fill="none" stroke="#c3a67c" stroke-width="1.3"/><line x1="6.3" y1="6.3" x2="9" y2="9" stroke="#c3a67c" stroke-width="1.3"/></svg></div>
<div class="abs rule" style="left:84px;top:48px;width:1035px"></div>

<div class="abs brand"><div class="brand-mark"></div><span class="brand-name">Tassino</span></div>
<div class="abs badge"></div>

<div class="abs cart-box">
  <div class="abs cart-icon"></div>
  <div class="abs cart-count">2</div>
  <div class="abs cart-text">Welcome Mira Lundqvist!<b>You have 2 items</b><b>in your shopping cart.</b></div>
  <div class="abs cart-bar">My shopping cart &nbsp;|&nbsp; Checkout</div>
</div>

<nav class="abs nav">
  <span class="abs nav-item" style="left:170px">BOY</span>
  <span class="abs nav-item" style="left:251px">GIRL</span>
  <span class="abs nav-item" style="left:328px">NEW PRODUCTS</span>
  <span class="abs nav-item" style="left:494px">BEST SELLERS</span>
  <span class="abs nav-div"></span>
  <span class="abs nav-item" style="left:668px">BLOG</span>
  <span class="abs nav-item" style="left:761px">INFORMATION</span>
</nav>

<div class="abs slider"></div>
<div class="abs hero" role="img" aria-label="Toddler in brown trousers and yellow shoes stepping down a stone curb"></div>
<div class="abs hero-legs"></div>
<div class="abs slogan">BIG SLOGAN</div>
<p class="abs slogan-copy">Lorem ipsum dolor sit amet, consectetur adipiscing elit. Vivamus ornare vehicula velit et rutrum.</p>
<svg class="abs arrow" style="left:234px" width="20" height="32" viewBox="0 0 20 32"><polyline points="16,2 4,16 16,30" fill="none" stroke="#ddd3c1" stroke-width="4"/></svg>
<svg class="abs arrow" style="left:949px" width="20" height="32" viewBox="0 0 20 32"><polyline points="4,2 16,16 4,30" fill="none" stroke="#ddd3c1" stroke-width="4"/></svg>
<div class="abs dots"><span></span><span class="on"></span><span></span><span></span></div>

<h2 class="abs section-title" style="font-weight:400">NEW PRODUCTS</h2>
<div class="abs rule" style="left:226px;top:621px;width:752px"></div>

<article class="abs card" style="left:226px">
  <h3 class="abs card-name" style="font-weight:400">PRODUCT 1 NAME</h3>
  <span class="abs card-desc">MINI DESCRIPTION</span>
  <svg class="abs ribbon" width="40" height="40" viewBox="0 0 40 40"><polygon points="4,0 18,0 40,22 40,36" fill="var(--wine)"/><text x="26" y="18" font-size="9" fill="#fff" font-family="Questrial,sans-serif" transform="rotate(45 26 18)" text-anchor="middle">new</text></svg>
  <div class="abs product-img"><div class="abs shoe" role="img" aria-label="Navy and light blue lace-up baby shoe" style="background:linear-gradient(#6fa6d6,#2a3f78 60%,#f0f0f0 85%)"></div></div>
  <span class="abs price">49,00€</span>
  <div class="abs btn-fav"><svg width="20" height="20" viewBox="0 0 20 20"><polygon points="10,1 12.6,7.3 19,7.6 14,11.8 15.7,18.5 10,14.8 4.3,18.5 6,11.8 1,7.6 7.4,7.3" fill="var(--wine)"/></svg></div>
  <div class="abs btn-cart"><svg width="20" height="20" viewBox="0 0 20 20" fill="none" stroke="#fff" stroke-width="1.5"><polyline points="1,3 4,3 6,13 16,13 18,6 5,6"/><circle cx="7" cy="16.5" r="1.5"/><circle cx="15" cy="16.5" r="1.5"/></svg></div>
</article>

<article class="abs card" style="left:487px">
  <h3 class="abs card-name" style="font-weight:400">PRODUCT 2 NAME</h3>
  <span class="abs card-desc">MINI DESCRIPTION</span>
  <svg class="abs ribbon" width="40" height="40" viewBox="0 0 40 40"><polygon points="4,0 18,0 40,22 40,36" fill="var(--wine)"/><text x="26" y="18" font-size="9" fill="#fff" font-family="Questrial,sans-serif" transform="rotate(45 26 18)" text-anchor="middle">new</text></svg>
  <div class="abs product-img"><div class="abs shoe" role="img" aria-label="Navy baby shoe with orange panels and zip" style="background:linear-gradient(#e07a3a,#243a70 50%,#f0f0f0 85%)"></div></div>
  <span class="abs price">49,00€</span>
  <div class="abs btn-fav"><svg width="20" height="20" viewBox="0 0 20 20"><polygon points="10,1 12.6,7.3 19,7.6 14,11.8 15.7,18.5 10,14.8 4.3,18.5 6,11.8 1,7.6 7.4,7.3" fill="var(--wine)"/></svg></div>
  <div class="abs btn-cart"><svg width="20" height="20" viewBox="0 0 20 20" fill="none" stroke="#fff" stroke-width="1.5"><polyline points="1,3 4,3 6,13 16,13 18,6 5,6"/><circle cx="7" cy="16.5" r="1.5"/><circle cx="15" cy="16.5" r="1.5"/></svg></div>
</article>

<article class="abs card" style="left:747px">
  <h3 class="abs card-name" style="font-weight:400">PRODUCT 3 NAME</h3>
  <span class="abs card-desc">MINI DESCRIPTION</span>
  <svg class="abs ribbon" width="40" height="40" viewBox="0 0 40 40"><polygon points="4,0 18,0 40,22 40,36" fill="var(--wine)"/><text x="26" y="18" font-size="9" fill="#fff" font-family="Questrial,sans-serif" transform="rotate(45 26 18)" text-anchor="middle">new</text></svg>
  <div class="abs product-img"><div class="abs shoe" role="img" aria-label="Teal baby shoe with velcro strap" style="background:linear-gradient(#2f7a86,#1f5a66 60%,#f0f0f0 85%)"></div></div>
  <span class="abs price">49,00€</span>
  <div class="abs btn-fav"><svg width="20" height="20" viewBox="0 0 20 20"><polygon points="10,1 12.6,7.3 19,7.6 14,11.8 15.7,18.5 10,14.8 4.3,18.5 6,11.8 1,7.6 7.4,7.3" fill="var(--wine)"/></svg></div>
  <div class="abs btn-cart"><svg width="20" height="20" viewBox="0 0 20 20" fill="none" stroke="#fff" stroke-width="1.5"><polyline points="1,3 4,3 6,13 16,13 18,6 5,6"/><circle cx="7" cy="16.5" r="1.5"/><circle cx="15" cy="16.5" r="1.5"/></svg></div>
</article>

<a class="abs view-more">view more</a>
</body>
</html>
```